New label for vitamin and supplement products

We are a a Vitamin and Supplement company called Brightmere. We have been in business for 30 years and the branding needs a significant refresh.

We need all new packaging, including logo, colors, etc.

We want to have a fresh, clean, brand that inspires confidence and quality.

The website is Brightmere.com and will also be updated.

Please ask any questions. Every idea is a good one.

```html
<!DOCTYPE html>
<html lang="en">
<head>
<meta charset="utf-8">
<title>Brightmere – Core Daily Minerals label</title>
<link href="https://fonts.googleapis.com/css2?family=Oswald:wght@700&family=Open+Sans:wght@600;700&display=swap" rel="stylesheet">
<style>
  :root {
    --backdrop: #2c4322;
    --label: #f4f4f2;
    --brand-green: #5e8a4a;
    --accent-green: #6c9a3d;
    --band-green: #4f7d40;
    --ink: #2b2b2b;
  }
  * { margin: 0; padding: 0; box-sizing: border-box; }
  html, body {
    width: 1200px;
    height: 810px;
    overflow: hidden;
    background: var(--backdrop);
  }
  .canvas {
    position: relative;
    width: 1200px;
    height: 810px;
    display: flex;
    align-items: center;
    justify-content: center;
  }
  .label {
    position: relative;
    width: 600px;
    height: 740px;
    background: var(--label);
    display: flex;
    flex-direction: column;
    align-items: center;
    font-family: "Open Sans", sans-serif;
  }
  .brand-name {
    margin-top: 150px;
    font-weight: 700;
    font-size: 74px;
    line-height: 1;
    color: var(--brand-green);
    letter-spacing: -1px;
  }
  .product-name {
    margin-top: 30px;
    font-family: "Oswald", sans-serif;
    font-weight: 700;
    font-size: 78px;
    line-height: 1.1;
    color: var(--ink);
    text-transform: uppercase;
    text-align: left;
    letter-spacing: -2px;
    margin-right: 20px;
  }
  .category {
    margin-top: 22px;
    font-weight: 600;
    font-size: 40px;
    line-height: 1;
    color: var(--accent-green);
    text-transform: uppercase;
    letter-spacing: 0.5px;
  }
  .tagline {
    margin-top: 16px;
    font-weight: 700;
    font-size: 29px;
    color: var(--ink);
  }
  .count {
    margin-top: 28px;
    font-weight: 700;
    font-size: 29px;
    color: var(--ink);
    text-transform: uppercase;
  }
  .base-band {
    position: absolute;
    left: 0;
    bottom: 58px;
    width: 100%;
    height: 30px;
  }
</style>
</head>
<body>
  <main class="canvas">
    <section class="label">
      <h1 class="brand-name">Brightmere</h1>
      <h2 class="product-name">Core Daily<br>Minerals</h2>
      <p class="category">Dietary Supplement</p>
      <p class="tagline">17 vitamin minerals</p>
      <p class="count">60 Caplets</p>
      <svg class="base-band" viewBox="0 0 600 30" preserveAspectRatio="none" aria-hidden="true">
        <rect x="0" y="0" width="600" height="14" fill="var(--band-green)"/>
        <rect x="0" y="20" width="600" height="6" fill="var(--band-green)"/>
      </svg>
    </section>
  </main>
</body>
</html>
```